Granola stand up bag packaging. Full Bleed printed on the bag. Full Color.

I Have a design I made but we are about to order thousands of printed bags so I thought I'd get a real designer to do the design. We do however want some sort of window area so the customer can see the granola through the bag. I have Illustrator native files of the logo for anyone who would like them. We have 3 flavors, so this is the first and we also have a coffee flavor, and a Oh Yeah flavor that we will need packaging for. The sample file is the package I designed myself, and like, however if we are going to pull the trigger on a $4,000 bag order then I want a design to use for the next 10 years!!

Target Market(s)

Granola Loving People at Natural Food Stores like Fernway Pantry.

Font styles to use
Sans Serif

Colors
acd036
ffffff
fbee3e

Requirements
Must have
• My logo, Some sort of transparent area so the customer can see the beautiful granola in the bag. Nutritional Facts and Bar Code area. Weight on the front of the bag.

```html
<!DOCTYPE html>
<html lang="en">
<head>
<meta charset="utf-8">
<title>Cascade Oat Works – Granola Package</title>
<link href="https://fonts.googleapis.com/css2?family=Open+Sans:wght@400;600;700&family=Oswald:wght@400&display=swap" rel="stylesheet">
<style>
  :root {
    --bg-top: #d3d2d3;
    --bg-bottom: #a9a9a9;
    --brand-green: #acd036;
    --side-green: #8fb52a;
    --brand-yellow: #fbee3e;
    --white: #ffffff;
    --ink: #111111;
    --label-ink: #2a2a2a;
    --frame: #050505;
    --granola-dark: #6b3f1f;
    --granola-mid: #a8733f;
    --granola-light: #c99a62;
    --logo-dark: #1f2a1a;
    --window-top: #c4c4c4;
    --window-bottom: #8f8f8f;
  }
  * { margin: 0; padding: 0; box-sizing: border-box; }
  html, body { width: 1200px; height: 1000px; overflow: hidden; }
  body {
    background: linear-gradient(180deg, var(--bg-top) 0%, var(--bg-bottom) 100%);
    font-family: "Open Sans", Arial, sans-serif;
    position: relative;
  }
  .package {
    position: absolute;
    left: 398px; top: 278px;
    width: 407px; height: 455px;
    display: flex;
  }
  /* Side panel */
  .side-panel {
    position: relative;
    width: 95px; height: 100%;
    background: var(--side-green);
    border-left: 8px solid var(--ink);
    overflow: hidden;
  }
  .side-logo {
    position: absolute; top: 10px; left: 0; right: 0;
    display: flex; flex-direction: column; align-items: center; gap: 4px;
  }
  .side-logo .mark {
    width: 16px; height: 16px; border-radius: 50%; background: var(--logo-dark);
  }
  .side-logo .name {
    font-family: "Open Sans", Arial, sans-serif; font-weight: 700;
    font-size: 7px; color: var(--logo-dark); text-align: center; line-height: 1.1;
    text-transform: uppercase;
  }
  .ingredients {
    position: absolute; left: 2px; top: 100px;
    width: 79px; height: 328px;
    background: var(--white);
    padding: 6px 3px;
    font-family: "Oswald", Arial, sans-serif;
    font-weight: 400;
    font-size: 7.6px; line-height: 16px; letter-spacing: -0.15px;
    color: var(--label-ink);
    overflow: hidden;
  }
  /* Front panel */
  .front-panel {
    position: relative;
    width: 312px; height: 100%;
    overflow: hidden;
  }
  .granola-fill {
    position: absolute; inset: 0;
    background:
      radial-gradient(circle at 80% 40%, var(--granola-light) 0%, transparent 45%),
      radial-gradient(circle at 15% 70%, var(--granola-mid) 0%, transparent 50%),
      linear-gradient(160deg, var(--granola-mid), var(--granola-dark));
  }
  .center-band {
    position: absolute; left: 78px; top: 0;
    width: 149px; height: 100%;
    background: var(--brand-green);
    border-left: 9px solid var(--brand-yellow);
    border-right: 9px solid var(--brand-yellow);
  }
  .brand-badge {
    position: absolute; left: 110px; top: 56px;
    width: 86px; height: 86px; border-radius: 50%;
    background: var(--logo-dark);
    border: 5px solid var(--side-green);
    display: flex; align-items: center; justify-content: center;
    text-align: center;
  }
  .brand-badge .name {
    font-weight: 700; font-size: 10px; line-height: 1.15;
    color: var(--white); text-transform: uppercase;
  }
  .window-frame {
    position: absolute; left: 58px; top: 217px;
    width: 189px; height: 158px;
    background: var(--frame);
    padding: 10px;
  }
  .window-frame .window {
    width: 100%; height: 100%;
    background: linear-gradient(180deg, var(--window-top), var(--window-bottom));
  }
  .net-weight {
    position: absolute; left: 78px; width: 149px; top: 416px;
    text-align: center; font-size: 21px; color: var(--ink);
  }
</style>
</head>
<body>
  <div class="package">
    <section class="side-panel">
      <div class="side-logo">
        <span class="mark"></span>
        <span class="name">Cascade<br>Oat Works</span>
      </div>
      <p class="ingredients">INGREDIENTS: Whole grain rolled oats, dried cranberries (cranberries, sugar, sunflower oil), maple syrup, sunflower seeds, almonds, pumpkin seeds, brown sugar, unsweetened desiccated coconut (with sodium metabisulfite to retain color), olive oil, unrefined cold pressed coconut oil, flax seeds, kosher salt, natural vanilla flavor, cinnamon, mixed tocopherols (Vitamin E to retain freshness). Contains tree nuts (almonds, coconut).</p>
    </section>
    <section class="front-panel">
      <div class="granola-fill" role="img" aria-label="Close-up photo of granola with oats, sliced almonds and dried cranberries"></div>
      <div class="center-band"></div>
      <div class="brand-badge"><span class="name">Cascade<br>Oat Works</span></div>
      <div class="window-frame"><div class="window"></div></div>
      <p class="net-weight">340 g</p>
    </section>
  </div>
</body>
</html>
```